New ante natal classes need competitive poster design

I am starting a new independent childbirth preparation business. There is a lot of competition from "trendy" practitioners locally. As an older and experienced childbirth educator I need to have a different appeal and image - That of experience/wisdom/grandmotherliness whilst being up to date with latest thinking . I am a mother of four and grandmother and have prepared over 1000 women for birth. The design needs to give a modern take on tradition with a mother and baby context. The name of my business is "tidal cradle", the poster will need to be sufficiently different to stand out on any notice board. Text as follows:
tidal cradle
Birth and parenthood classes using the most effective preparation techniques run by experienced BPA teacher/trainer
Classes cover:
choices in childbirth
normal pregnancy, labour and variations
self help techniques for labour including hypno-birthing
breastfeeding
baby care and paediatric first aid

Call 07448213097

```html
<!DOCTYPE html>
<html lang="en">
<head>
<meta charset="utf-8">
<title>Tidal Cradle – Birth and Parenthood Classes</title>
<link rel="stylesheet" href="https://fonts.googleapis.com/css2?family=Cinzel:wght@400&family=Arimo:wght@400;700&family=Bitter:wght@700&display=swap">
<style>
  :root {
    --night: #0b0b0b;
    --claret: #7e282b;
    --paper: #ffffff;
    --grey-light: #d9d9d9;
    --grey-mid: #8c8c8c;
    --grey-dark: #3a3a3a;
  }
  * { margin: 0; padding: 0; box-sizing: border-box; }
  html, body {
    width: 1200px;
    height: 849px;
    overflow: hidden;
    background: var(--paper);
  }
  .poster {
    position: relative;
    width: 1200px;
    height: 849px;
    overflow: hidden;
    color: var(--paper);
  }
  .intro {
    position: absolute;
    left: 0; top: 0;
    width: 1200px;
    height: 428px;
    background: var(--night);
  }
  .brand-name {
    position: absolute;
    left: 48px;
    top: 42px;
    font-family: "Cinzel", "Trajan Pro", serif;
    font-weight: 400;
    font-size: 80px;
    line-height: 1;
    letter-spacing: 2px;
    white-space: nowrap;
  }
  .tagline {
    position: absolute;
    left: 48px;
    top: 190px;
    width: 688px;
    font-family: "Arimo", Arial, sans-serif;
    font-size: 32px;
    line-height: 45px;
    text-align: justify;
    text-align-last: left;
  }
  .tagline strong { font-weight: 700; }
  .mother-baby-art {
    position: absolute;
    left: 782px;
    top: 26px;
    width: 402px;
    height: 402px;
    border-radius: 50%;
    background: radial-gradient(circle at 45% 45%, var(--grey-light) 0%, var(--grey-mid) 60%, var(--grey-dark) 100%);
    border: 2px solid var(--grey-dark);
  }
  .courses {
    position: absolute;
    left: 0; top: 428px;
    width: 1200px;
    height: 421px;
    background: var(--claret);
  }
  .courses-heading {
    position: absolute;
    left: 56px;
    top: 20px;
    font-family: "Arimo", Arial, sans-serif;
    font-weight: 400;
    font-size: 30px;
    letter-spacing: 13px;
    line-height: 1;
  }
  .course-list {
    position: absolute;
    left: 54px;
    top: 72px;
    list-style: none;
    font-family: "Bitter", Georgia, serif;
    font-weight: 700;
    font-size: 28px;
  }
  .course-list li { height: 48.5px; line-height: 40px; }
  .call-to-action {
    position: absolute;
    right: 53px;
    bottom: 18px;
    font-family: "Arimo", Arial, sans-serif;
    font-weight: 700;
    font-size: 64px;
    line-height: 1;
    white-space: nowrap;
  }
</style>
</head>
<body>
<main class="poster">
  <section class="intro">
    <h1 class="brand-name">Tidal Cradle</h1>
    <p class="tagline">Birth and parenthood classes using the most effective preparation techniques run by experienced <strong>BPA teacher/trainer</strong></p>
    <div class="mother-baby-art" role="img" aria-label="Circular posterised greyscale illustration of a grandmother holding a baby close"></div>
  </section>
  <section class="courses">
    <h2 class="courses-heading">CLASSES COVER</h2>
    <ul class="course-list">
      <li>Choices in childbirth</li>
      <li>Normal pregnancy, labour and variations</li>
      <li>Self help techniques for labour including hypno-birthing</li>
      <li>Breastfeeding</li>
      <li>Baby care and paediatric first aid</li>
    </ul>
    <p class="call-to-action">Call 07448213097</p>
  </section>
</main>
</body>
</html>
```